Business Card Design

we specialise in supply of custom uniforms - teamwear to Schools and sporting clubs, see our website: www.harbourkitcove.com.au, our main corporate colour is black and white, with small amount of gold/yellow

Industry/Entity Type

Business

Contact Information for Business Card

Harbour Kit Cove
Travis Okafor
Ph 03 6218 5097
Mobile 0462 318 740
email: travis@harbourkitcove.com.au
www.harbourkitcove.com.au
like us on facebook

Requirements
Must have
• modern look & feel

```html
<!DOCTYPE html>
<html lang="en">
<head>
<meta charset="utf-8">
<title>Harbour Kit Cove – Business Card</title>
<link rel="stylesheet" href="https://fonts.googleapis.com/css2?family=Source+Sans+3:wght@400;600&display=swap">
<style>
  :root {
    --canvas-bg: #d9d6d2;
    --ink-black: #050505;
    --panel-dark: #1b1b1b;
    --panel-mid: #2e2e2e;
    --paper-white: #f4f4f4;
    --accent-gold: #d8b63a;
    --text-white: #ffffff;
    --text-dark: #141414;
  }
  html, body {
    margin: 0;
    padding: 0;
    width: 1200px;
    height: 1200px;
    overflow: hidden;
    background: var(--canvas-bg);
  }
  .business-card {
    position: absolute;
    left: 100px;
    top: 300px;
    width: 1000px;
    height: 600px;
    filter: drop-shadow(0 14px 24px rgba(0,0,0,0.35));
  }
  .card-text {
    font-family: "Source Sans 3", "Myriad Pro", sans-serif;
  }
  .brand-name { fill: var(--text-white); font-weight: 600; font-size: 30px; }
  .web-address { fill: var(--text-dark); font-weight: 400; font-size: 30px; letter-spacing: 0.5px; }
  .person-name { fill: var(--text-white); font-weight: 600; font-size: 30px; }
  .contact-line { fill: var(--accent-gold); font-weight: 400; font-size: 26px; }
  .contact-icon { fill: none; stroke: var(--accent-gold); stroke-width: 2; }
  .contact-icon-fill { fill: var(--accent-gold); }
</style>
</head>
<body>
<svg class="business-card" viewBox="0 0 1000 600" xmlns="http://www.w3.org/2000/svg">
  <defs>
    <linearGradient id="leftPanel" x1="0" y1="0" x2="1" y2="0">
      <stop offset="0" stop-color="#020202"/>
      <stop offset="1" stop-color="#161616"/>
    </linearGradient>
    <linearGradient id="topPanel" x1="0" y1="0" x2="1" y2="1">
      <stop offset="0" stop-color="#111111"/>
      <stop offset="1" stop-color="#242424"/>
    </linearGradient>
    <linearGradient id="bottomPanel" x1="0" y1="0" x2="0" y2="1">
      <stop offset="0" stop-color="#121212"/>
      <stop offset="1" stop-color="#333333"/>
    </linearGradient>
    <linearGradient id="whitePanel" x1="0" y1="0" x2="1" y2="1">
      <stop offset="0" stop-color="#ffffff"/>
      <stop offset="1" stop-color="#e6e6e6"/>
    </linearGradient>
  </defs>

  <!-- card panels -->
  <polygon class="panel-left" points="0,0 540,150 0,600" fill="url(#leftPanel)"/>
  <polygon class="panel-top" points="0,0 650,0 540,150" fill="url(#topPanel)"/>
  <polygon class="panel-bottom" points="0,600 1000,600 540,150" fill="url(#bottomPanel)"/>
  <polygon class="panel-white" points="650,0 1000,0 1000,600 540,150" fill="url(#whitePanel)"/>

  <!-- brand -->
  <text class="card-text brand-name" transform="translate(300,260) rotate(-45)">Harbour Kit Cove</text>

  <!-- web address along the diagonal -->
  <text class="card-text web-address" transform="translate(588,160) rotate(44.4)">www.harbourkitcove.com.au</text>

  <!-- contact block -->
  <text class="card-text person-name" x="520" y="468" text-anchor="middle">Travis Okafor</text>

  <g class="phone-line">
    <circle class="contact-icon" cx="290" cy="511" r="11"/>
    <path class="contact-icon-fill" d="M285 504 q-2 7 4 14 q6 6 10 4 l-3 -4 q-2 1 -4 -1 q-4 -4 -3 -7 l-1 -4 z"/>
    <text class="card-text contact-line" x="308" y="520">Ph 03 6218 5097</text>
    <text class="card-text contact-line" x="510" y="520">Mobile 0462 318 740</text>
  </g>

  <g class="email-line">
    <circle class="contact-icon" cx="290" cy="553" r="11"/>
    <rect class="contact-icon-fill" x="283" y="548" width="14" height="10" rx="1"/>
    <path d="M283 548 l7 6 l7 -6" fill="none" stroke="#1e1e1e" stroke-width="1.5"/>
    <text class="card-text contact-line" x="308" y="562">email: travis@harbourkitcove.com.au</text>
  </g>
</svg>
</body>
</html>
```